Kambo Flyer

to create a Flyer with information about Kambo Ceremonies. The flyer that is up loaded is an example

Requirements
Must have
• Benefits of Kambo
• Kambo is traditionally known to be anti-inflammatory, to relieve joint pain, to heal eyesight, and to ease pain. Kambo peptides, and their effects, are reported to cover a wide range of potential medical uses: treatment of brain diseases such as Alzheimer’s and Parkinson’s, depression, migraines, blood circulation problems, vascular insufficiency, organ diseases, skin and eyes issues, cancer, fertility problems in women, AIDS, candida, hepatitis, herpes, and more
• What is Kambo
• The scientific name for this frog is Phyllomedusa bicolor or “Two-Colored Leaf Guardian.” It is also known as the “Giant Green Monkey Tree Frog.”
• Kambo is legal in the United States, as well as all other countries, and is not a hallucinogenic. It is, however, a deep cleansing therapy – – physically, emotionally and mentally. It is one of the world’s most effective and natural antibiotics and immune system boosters. It detoxifies the liver and intestines, improves mental functioning, and has the potential to dissolve emotional blocks. It also helps to reset our cellular memory.
• Please note that fasting 12 hours prior to the ceremony is required
• Private (in Home} Semi-Private and Group Ceremonies Available
• For More information see our website
• www.MeadowLightHalls.org
• 555-214-0873
• Traditional Shamanic Kambo Ceremonies in Florida

```html
<!DOCTYPE html>
<html lang="en">
<head>
<meta charset="UTF-8">
<title>Kambo Ceremonies Flyer</title>
<link href="https://fonts.googleapis.com/css2?family=Fraunces:opsz,wght@72,900&family=Lato:wght@300;400;700&display=swap" rel="stylesheet">
<style>
  :root {
    --stage: #d8d8d8;
    --paper: #ffffff;
    --ink: #1d1d1d;
    --body-ink: #444444;
    --sunset-top: #3a3550;
    --sunset-mid: #d8553a;
    --sunset-glow: #f29a4a;
    --sea: #5a2a30;
    --forest-dark: #0f2a14;
    --forest: #1f5a25;
    --leaf: #3f8f2f;
    --white: #ffffff;
  }
  * { margin: 0; padding: 0; box-sizing: border-box; }
  html, body { width: 1200px; height: 1000px; overflow: hidden; }
  body {
    background: var(--stage);
    font-family: "Lato", Arial, sans-serif;
    position: relative;
  }
  .flyer {
    position: absolute;
    left: 323px; top: 107px;
    width: 546px; height: 772px;
    background: var(--paper);
    overflow: hidden;
    box-shadow: 0 6px 18px rgba(0,0,0,0.25);
  }
  .hero {
    position: absolute; left: 0; top: 0; width: 546px; height: 172px;
    background:
      radial-gradient(ellipse 120px 40px at 400px 100px, var(--sunset-glow), transparent 70%),
      linear-gradient(180deg, var(--sunset-top) 0%, #7a3a4a 30%, var(--sunset-mid) 55%, #a8383a 72%, var(--sea) 100%);
  }
  .hero-wave, .footer-wave { position: absolute; left: 0; width: 546px; display: block; }
  .hero-wave { top: 130px; height: 45px; }
  .hero-title { position: absolute; left: 43px; top: 26px; color: var(--white); z-index: 2; }
  .hero-kicker, .hero-sub { font-size: 17px; font-weight: 400; line-height: 1; }
  .hero-name {
    font-family: "Fraunces", Georgia, serif;
    font-weight: 900; font-size: 60px; line-height: 0.9; margin: 0 0 2px; letter-spacing: 0.5px;
  }
  .content { position: absolute; left: 44px; top: 170px; width: 453px; color: var(--body-ink); }
  .section-title { font-size: 14.5px; font-weight: 400; color: var(--ink); margin-bottom: 4px; }
  .content p {
    font-size: 10.6px; font-weight: 400; line-height: 13px;
    text-align: justify; margin-bottom: 7px;
  }
  .content strong { font-weight: 400; color: var(--ink); }
  .content .what { margin-top: 10px; }
  .practitioners-title {
    position: absolute; left: 44px; top: 437px;
    font-size: 14.5px; font-weight: 400; color: var(--ink);
  }
  .portrait {
    position: absolute; top: 466px; width: 110px; height: 110px; border-radius: 50%;
    box-shadow: 0 3px 8px rgba(0,0,0,0.35);
  }
  .portrait-one { left: 75px; background: radial-gradient(circle at 50% 40%, #c9a585, #5b6e7a 70%, #34404a); }
  .portrait-two { left: 211px; background: radial-gradient(circle at 50% 40%, #d9b08a, #efe6de 70%, #f6f2ee); }
  .portrait-three { left: 346px; background: radial-gradient(circle at 50% 35%, #f08a2a, #6a3a1a 55%, #1a1512); }
  .notes {
    position: absolute; left: 42px; top: 595px; z-index: 3;
    font-size: 10.8px; line-height: 17px; color: var(--ink);
  }
  .footer {
    position: absolute; left: 0; top: 632px; width: 546px; height: 140px;
    background: linear-gradient(90deg, var(--forest-dark) 0%, #143a18 50%, var(--forest) 100%);
  }
  .footer-photo {
    position: absolute; right: 0; top: 0; width: 250px; height: 140px;
    background: radial-gradient(ellipse 90px 50px at 140px 80px, #4faa38, var(--leaf) 40%, transparent 80%);
  }
  .footer-wave { top: 0; height: 42px; }
  .contact { position: absolute; left: 38px; top: 687px; color: var(--white); z-index: 2; }
  .contact-lead { font-size: 12.5px; font-weight: 400; }
  .contact-web { font-size: 12.5px; font-weight: 700; letter-spacing: 0.6px; margin-top: 1px; }
  .contact-call { font-size: 17px; font-weight: 700; margin-top: 12px; }
</style>
</head>
<body>
  <main class="flyer">
    <div class="hero" role="img" aria-label="Sunset over the sea with a person standing arms outstretched on the shore"></div>
    <svg class="hero-wave" viewBox="0 0 546 45" preserveAspectRatio="none" aria-hidden="true">
      <path d="M0 22 C120 0 200 0 300 18 C400 36 480 40 546 30 L546 45 L0 45 Z" fill="#ffffff"/>
    </svg>
    <header class="hero-title">
      <div class="hero-kicker">Traditional Shamanic</div>
      <h1 class="hero-name">Kambo</h1>
      <div class="hero-sub">Ceremonies in Florida</div>
    </header>

    <section class="content">
      <h2 class="section-title">Benefits of Kambo</h2>
      <p>Kambo is traditionally known to be anti-inflammatory, to relieve joint pain, to heal eyesight, and to ease pain.</p>
      <p>Kambo peptides, and their effects, are reported to cover a wide range of potential medical uses: treatment of brain diseases such as Alzheimer’s and Parkinson’s, depression, migraines, blood circulation problems, vascular insufficiency, organ diseases, skin and eyes issues, cancer, fertility problems in women, AIDS, candida, hepatitis, herpes, and more</p>
      <h2 class="section-title what">What is Kambo</h2>
      <p>The scientific name for this frog is Phyllomedusa bicolor or <strong>“Two-Colored Leaf Guardian.”</strong> It is also known as the <strong>“Giant Green Monkey Tree Frog.”</strong></p>
      <p>Kambo is legal in the United States, as well as all other countries, and is not a hallucinogenic. It is, however, a deep cleansing therapy–physically, emotionally and mentally. It is one of the world’s most effective and natural antibiotics and immune system boosters. It detoxifies the liver and intestines, improves mental functioning, and has the potential to dissolve emotional blocks. It also helps to reset our cellular memory.</p>
    </section>

    <h2 class="practitioners-title">Our practitioners</h2>
    <div class="portrait portrait-one" role="img" aria-label="Portrait of a practitioner wearing a beaded necklace"></div>
    <div class="portrait portrait-two" role="img" aria-label="Portrait of a practitioner in a white top"></div>
    <div class="portrait portrait-three" role="img" aria-label="Portrait of a practitioner in front of a fire"></div>

    <footer class="footer">
      <div class="footer-photo" role="img" aria-label="Green tree frog with red eyes sitting on a leaf"></div>
      <svg class="footer-wave" viewBox="0 0 546 42" preserveAspectRatio="none" aria-hidden="true">
        <path d="M0 0 L546 0 L546 2 C440 0 340 10 250 24 C160 38 70 36 0 26 Z" fill="#ffffff"/>
      </svg>
    </footer>

    <div class="notes">
      <p>Please note that fasting 12 hours prior to the ceremony is required.</p>
      <p>Private (in Home} Semi-Private and</p>
      <p>Group Ceremonies Available.</p>
    </div>

    <div class="contact">
      <div class="contact-lead">For More information see our website:</div>
      <div class="contact-web">www.MeadowLightHalls.org</div>
      <div class="contact-call">Call Us NOW: 555-214-0873</div>
    </div>
  </main>
</body>
</html>
```